Tease by Dusk Age Verification Landing Page

To create a visually appealing design for the landing page of the adult game "Tease by Dusk" that confirms the visitor's age.
The design should have a simple and visually appealing look that focuses on two buttons labeled "Yes" and "No". The purpose of the page is to confirm that the visitor is 18 years of age or older before accessing the game's content. Responsive design that works well on desktop and mobile devices. The final output should be delivered in PSD, AI, or Sketch format, along with any necessary images or assets.
I have also attached examples.

```html
<!DOCTYPE html>
<html lang="en">
<head>
<meta charset="utf-8">
<title>Tease by Dusk — Age Verification</title>
<link href="https://fonts.googleapis.com/css2?family=Plus+Jakarta+Sans:wght@400;600;700;800&family=Outfit:wght@400;500;600&display=swap" rel="stylesheet">
<style>
  :root{
    --board:#f4f4f4;
    --board-soft:#ececec;
    --label:#0a0a0a;
    --brand:#c263c2;
    --page:#000000;
    --ghost:#1c1c1f;
    --ghost-soft:#151517;
    --ghost-line:#202024;
    --ghost-accent:#3a2608;
    --ghost-violet:#17122c;
    --badge-top:#c472c4;
    --badge-mid:#e382dc;
    --badge-bottom:#b258b0;
    --frame-line:rgba(255,255,255,.8);
    --ink-light:#ffffff;
    --ink-soft:#f3c9ef;
    --btn-pink-top:#dc78d8;
    --btn-pink-bottom:#8a2c8f;
    --btn-dark-top:#2a2a2a;
    --btn-dark-bottom:#050505;
  }
  *{box-sizing:border-box;margin:0;padding:0}
  html,body{width:1200px;height:874px;overflow:hidden}
  body{position:relative;font-family:"Plus Jakarta Sans",sans-serif;
    background:linear-gradient(135deg,var(--board) 0%,#fbfbfb 45%,var(--board-soft) 100%)}

  /* brand showcase */
  .showcase-mark{position:absolute;left:573px;top:30px;width:60px;height:60px;border-radius:50%;background:var(--brand)}
  .showcase-name{position:absolute;left:0;right:0;top:136px;text-align:center;padding-left:6px;
    font-size:21px;font-weight:700;color:var(--brand)}

  .view-label{position:absolute;font-size:15px;font-weight:800;color:var(--label);letter-spacing:.01em}
  .view-label.desktop{left:176px;top:195px}
  .view-label.mobile{left:842px;top:193px}

  /* screens, built at full size then scaled */
  .screen{position:absolute;background:var(--page);overflow:hidden;transform-origin:0 0;transform:scale(.529)}
  .screen.desktop{left:177px;top:236px;width:1134px;height:907px}
  .screen.mobile{left:847px;top:229px;width:332px;height:654px}

  /* dimmed site behind the gate */
  .site{position:absolute;inset:0;font-family:"Outfit",sans-serif;color:var(--ghost)}
  .site-brand{position:absolute;left:-4px;top:18px;font-size:22px;font-weight:500}
  .site-nav{position:absolute;left:292px;top:24px;display:flex;gap:25px;font-size:14px}
  .site-actions{position:absolute;left:857px;top:12px;display:flex;gap:10px}
  .ghost-btn{height:30px;padding:0 12px;border:1px solid var(--ghost-line);border-radius:8px;display:flex;align-items:center;
    font-size:9px;letter-spacing:.08em;color:var(--ghost)}
  .ghost-btn.filled{background:var(--ghost-accent);border-color:var(--ghost-accent)}
  .ghost-btn.violet{background:var(--ghost-violet);border-color:var(--ghost-violet)}
  .hero-title{position:absolute;left:-42px;top:200px;font-size:64px;line-height:70px;font-weight:600;letter-spacing:-.5px;white-space:nowrap}
  .hero-copy{position:absolute;left:-30px;top:352px;font-size:18px;line-height:26px;color:var(--ghost-soft);white-space:nowrap}
  .hero-actions{position:absolute;left:-50px;top:428px;display:flex;gap:12px}
  .hero-actions .ghost-btn{height:40px;padding:0 16px}
  .hero-art{position:absolute;left:680px;top:120px;width:420px;height:450px;border-radius:30px;
    background:radial-gradient(circle at 50% 45%,#22161f 0%,#120c12 50%,rgba(0,0,0,0) 78%)}
  .update-title{position:absolute;left:24px;top:688px;font-size:36px;line-height:40px;font-weight:600}
  .update-copy{position:absolute;left:24px;top:780px;font-size:15px;line-height:20px;color:var(--ghost-soft)}
  .update-actions{position:absolute;left:24px;top:838px;display:flex;gap:12px}
  .update-actions .ghost-btn{height:38px;padding:0 26px}
  .class-row{position:absolute;left:490px;top:745px;width:460px;height:100px;border-radius:50px;
    background:linear-gradient(90deg,#120b1c,#0b1510,#1a0e06,#081220)}

  /* mobile status bar */
  .status-time{position:absolute;left:18px;top:13px;font-size:11px;font-weight:600;color:var(--ink-light)}
  .status-icons{position:absolute;right:12px;top:12px;width:60px;height:12px}

  /* age gate, 255 x 616 */
  .gate{position:absolute;width:255px;height:616px;transform-origin:0 0}
  .screen.desktop .gate{left:440px;top:146px}
  .screen.mobile .gate{left:73px;top:84px;transform:scale(.796)}
  .gate-frame{position:absolute;inset:0;width:100%;height:100%}
  .gate-mark{position:absolute;left:84px;top:92px;width:88px;height:88px;border-radius:50%;background:var(--ink-light)}
  .gate-brand{position:absolute;left:0;right:0;top:303px;text-align:center;font-size:25px;font-weight:700;color:var(--ink-light)}
  .gate-question{position:absolute;left:0;right:0;top:380px;text-align:center;font-size:13px;font-weight:700;color:var(--ink-light)}
  .gate-btn{position:absolute;left:36px;width:183px;height:40px;border-radius:20px;display:flex;align-items:center;justify-content:center;
    font-size:14px;font-weight:700;color:var(--ink-light)}
  .gate-btn.confirm{top:416px;background:linear-gradient(var(--btn-pink-top),var(--btn-pink-bottom));box-shadow:0 2px 4px rgba(90,20,90,.35)}
  .gate-btn.leave{top:471px;background:linear-gradient(var(--btn-dark-top),var(--btn-dark-bottom));box-shadow:0 2px 4px rgba(0,0,0,.35)}
  .gate-remember{position:absolute;left:0;right:0;top:533px;display:flex;align-items:center;justify-content:center;gap:9px;
    font-size:11px;letter-spacing:.04em;color:var(--ink-soft)}
  .gate-remember .box{width:11px;height:11px;border-radius:1px;background:var(--ink-soft)}
</style>
</head>
<body>
  <header class="showcase" aria-label="Brand">
    <span class="showcase-mark" aria-hidden="true"></span>
    <p class="showcase-name">Tease by Dusk</p>
  </header>

  <h2 class="view-label desktop">DESKTOP VIEW</h2>
  <h2 class="view-label mobile">MOBILE VIEW</h2>

  <svg width="0" height="0" style="position:absolute" aria-hidden="true">
    <defs>
      <linearGradient id="badgeFill" x1="0" y1="0" x2="0" y2="1">
        <stop offset="0" stop-color="#c472c4"/>
        <stop offset=".45" stop-color="#e382dc"/>
        <stop offset="1" stop-color="#b258b0"/>
      </linearGradient>
    </defs>
  </svg>

  <div class="screen desktop">
    <div class="site" aria-hidden="true">
      <div class="site-brand">Arcana</div>
      <nav class="site-nav"><span>Overview</span><span>Features</span><span>Getting Started</span><span>Media</span><span>FAQ</span></nav>
      <div class="site-actions"><span class="ghost-btn">ACCOUNT</span><span class="ghost-btn filled">SUBSCRIBE</span></div>
      <div class="hero-art" role="img" aria-label="Game characters illustration"></div>
      <h1 class="hero-title">Beautiful game,<br>intense reality</h1>
      <p class="hero-copy">Welcome to Arcana, the strategy card game<br>easy to learn but impossible to put down!</p>
      <div class="hero-actions"><span class="ghost-btn violet">BUY NOW</span><span class="ghost-btn">LEARN MORE</span></div>
      <h2 class="update-title">Synergy of the light<br>update is now live</h2>
      <p class="update-copy">Combine new spells and character abilities however you<br>want. Create your own classes and share your decks.</p>
      <div class="update-actions"><span class="ghost-btn violet">BUY NOW</span><span class="ghost-btn">LEARN MORE</span></div>
      <div class="class-row" role="img" aria-label="Row of character class emblems"></div>
    </div>

    <section class="gate" aria-label="Age verification">
      <svg class="gate-frame" viewBox="0 0 255 616" aria-hidden="true">
        <path fill="url(#badgeFill)" d="M48 52 L48 22 Q127.5 -22 207 22 L207 52 Q255 54 255 104 L255 512 Q255 562 207 564 L207 594 Q127.5 638 48 594 L48 564 Q0 562 0 512 L0 104 Q0 54 48 52 Z"/>
        <path fill="none" stroke="var(--frame-line)" stroke-width="1.5" d="M60 64 L60 34 Q127.5 2 195 34 L195 64 Q243 66 243 112 L243 504 Q243 550 195 552 L195 582 Q127.5 614 60 582 L60 552 Q12 550 12 504 L12 112 Q12 66 60 64 Z"/>
      </svg>
      <span class="gate-mark" aria-hidden="true"></span>
      <p class="gate-brand">Tease by Dusk</p>
      <p class="gate-question">Are you over 18 years of age?</p>
      <div class="gate-btn confirm">I'M OVER 18</div>
      <div class="gate-btn leave">EXIT</div>
      <div class="gate-remember"><span class="box"></span>Remember me</div>
    </section>
  </div>

  <div class="screen mobile">
    <span class="status-time">11.00AM</span>
    <svg class="status-icons" viewBox="0 0 60 12" aria-hidden="true">
      <path d="M4 5 Q10 0 16 5" fill="none" stroke="#fff" stroke-width="1.4"/>
      <path d="M6.5 7.5 Q10 4.5 13.5 7.5" fill="none" stroke="#fff" stroke-width="1.4"/>
      <circle cx="10" cy="10" r="1.3" fill="#fff"/>
      <rect x="24" y="8" width="1.6" height="3" fill="#fff"/>
      <rect x="27" y="6" width="1.6" height="5" fill="#fff"/>
      <rect x="30" y="4" width="1.6" height="7" fill="#fff"/>
      <rect x="33" y="2" width="1.6" height="9" fill="#fff"/>
      <rect x="42" y="3" width="15" height="7" rx="1.5" fill="none" stroke="#fff" stroke-width="1"/>
      <rect x="43.5" y="4.5" width="12" height="4" fill="#fff"/>
    </svg>

    <section class="gate" aria-label="Age verification">
      <svg class="gate-frame" viewBox="0 0 255 616" aria-hidden="true">
        <path fill="url(#badgeFill)" d="M48 52 L48 22 Q127.5 -22 207 22 L207 52 Q255 54 255 104 L255 512 Q255 562 207 564 L207 594 Q127.5 638 48 594 L48 564 Q0 562 0 512 L0 104 Q0 54 48 52 Z"/>
        <path fill="none" stroke="var(--frame-line)" stroke-width="1.5" d="M60 64 L60 34 Q127.5 2 195 34 L195 64 Q243 66 243 112 L243 504 Q243 550 195 552 L195 582 Q127.5 614 60 582 L60 552 Q12 550 12 504 L12 112 Q12 66 60 64 Z"/>
      </svg>
      <span class="gate-mark" aria-hidden="true"></span>
      <p class="gate-brand">Tease by Dusk</p>
      <p class="gate-question">Are you over 18 years of age?</p>
      <div class="gate-btn confirm">I'M OVER 18</div>
      <div class="gate-btn leave">EXIT</div>
      <div class="gate-remember"><span class="box"></span>Remember me</div>
    </section>
  </div>
</body>
</html>
```